CareLumen business cards

We need a business card design that we could customize as needed for employees. We will need space for Name, Title, 1-2 phone numbers and email address.

We are a Pharmacy Benefits Management (PBM) company for hospice agencies and beginning a nationwide expansion. Attached is a vector file of our logo.

Cards can be single or double sided.

```html
<!DOCTYPE html>
<html lang="en">
<head>
<meta charset="utf-8">
<title>CareLumen business cards</title>
<link href="https://fonts.googleapis.com/css2?family=Questrial&display=swap" rel="stylesheet">
<style>
  :root {
    --page: #e8e7e3;
    --card: #fbfbfa;
    --green: #8fae5a;
    --blue: #2b86b8;
    --ink: #4f5256;
    --muted: #7a7d80;
  }
  * { margin: 0; padding: 0; box-sizing: border-box; }
  html, body { width: 1171px; height: 1200px; overflow: hidden; }
  body {
    background: var(--page);
    font-family: "Questrial", "Century Gothic", sans-serif;
    color: var(--ink);
    position: relative;
  }
  .card {
    position: absolute;
    left: 135px;
    width: 900px;
    height: 514px;
    background: var(--card);
    border-radius: 26px;
    overflow: hidden;
    box-shadow: 0 6px 18px rgba(0,0,0,0.12);
  }
  .card-front { top: 56px; }
  .card-back { top: 630px; }
  .edge-band {
    position: absolute;
    left: 0; bottom: 0;
    width: 900px; height: 60px;
  }
  .edge-band .band-green { fill: var(--green); }
  .edge-band .band-blue { fill: var(--blue); }

  .brand {
    position: absolute;
    display: flex;
    align-items: center;
    gap: 22px;
  }
  .brand-square {
    width: 58px; height: 58px;
    background: var(--green);
  }
  .brand-name {
    font-size: 72px;
    color: var(--blue);
    letter-spacing: -1px;
    line-height: 1;
  }
  .card-front .brand { left: 120px; top: 170px; }
  .tagline {
    position: absolute;
    left: 304px; top: 272px;
    font-size: 19px;
    letter-spacing: 5px;
    color: var(--ink);
  }

  .card-back .brand { left: 80px; top: 80px; }
  .card-back .brand-square { width: 44px; height: 44px; }
  .card-back .brand-name { font-size: 56px; }
  .person {
    position: absolute;
    right: 80px; top: 82px;
    text-align: right;
  }
  .person-name {
    font-size: 30px;
    color: var(--green);
    letter-spacing: 1px;
    font-weight: 700;
  }
  .person-title {
    font-size: 15px;
    letter-spacing: 2px;
    color: var(--ink);
    margin-top: 6px;
  }
  .contact-tab {
    position: absolute;
    left: 0; top: 246px;
    width: 64px; height: 176px;
    background: var(--green);
    border-radius: 0 16px 16px 0;
    display: flex;
    flex-direction: column;
    justify-content: space-around;
    align-items: center;
    padding: 10px 0;
  }
  .contact-tab svg { width: 22px; height: 22px; }
  .contact-list {
    position: absolute;
    left: 96px; top: 258px;
    list-style: none;
    font-size: 19px;
    line-height: 36px;
    color: var(--ink);
  }
</style>
</head>
<body>

<section class="card card-front">
  <div class="brand">
    <span class="brand-square"></span>
    <span class="brand-name">CareLumen</span>
  </div>
  <p class="tagline">PHARMACY BENEFITS MANAGEMENT</p>
  <svg class="edge-band" viewBox="0 0 900 60" aria-hidden="true">
    <rect class="band-green" x="0" y="42" width="900" height="18"/>
    <path class="band-blue" d="M640 60 C668 60 664 24 700 24 L900 24 L900 60 Z"/>
  </svg>
</section>

<section class="card card-back">
  <div class="brand">
    <span class="brand-square"></span>
    <span class="brand-name">CareLumen</span>
  </div>
  <div class="person">
    <p class="person-name">YOUR NAME</p>
    <p class="person-title">DESIGNATION</p>
  </div>
  <div class="contact-tab" aria-hidden="true">
    <svg viewBox="0 0 24 24"><path fill="#fff" d="M6.6 10.8a15 15 0 0 0 6.6 6.6l2.2-2.2a1 1 0 0 1 1-.25 11.4 11.4 0 0 0 3.6.57 1 1 0 0 1 1 1V20a1 1 0 0 1-1 1A17 17 0 0 1 3 4a1 1 0 0 1 1-1h3.5a1 1 0 0 1 1 1c0 1.25.2 2.45.57 3.57a1 1 0 0 1-.25 1z"/></svg>
    <svg viewBox="0 0 24 24"><path fill="#fff" d="M6 2h12v6H6zM4 9h16a2 2 0 0 1 2 2v6h-4v5H6v-5H2v-6a2 2 0 0 1 2-2zm4 7v4h8v-4z"/></svg>
    <svg viewBox="0 0 24 24"><path fill="#fff" d="M3 5h18v14H3zm2 2v.5l7 4.5 7-4.5V7l-7 4.5z"/></svg>
    <svg viewBox="0 0 24 24"><path fill="#fff" d="M12 2a7 7 0 0 0-7 7c0 5 7 13 7 13s7-8 7-13a7 7 0 0 0-7-7zm0 9.5A2.5 2.5 0 1 1 12 6.5a2.5 2.5 0 0 1 0 5z"/></svg>
  </div>
  <ul class="contact-list">
    <li>07 4810 2261</li>
    <li>07 4810 2274</li>
    <li>info@carelumen.com</li>
    <li>Your Complete<br>Address Details Here</li>
  </ul>
  <svg class="edge-band" viewBox="0 0 900 60" aria-hidden="true">
    <rect class="band-green" x="0" y="42" width="900" height="18"/>
    <path class="band-blue" d="M640 60 C668 60 664 24 700 24 L900 24 L900 60 Z"/>
  </svg>
</section>

</body>
</html>
```